Managed Service Provider need new business cards

We are a small Maanged Service Provider of IT Services and need a new fresh design for our business cards. We want something impossible, fun and professional :)
Our services has a large range, but we are always fun and make sure our customers both get their issue sorted and also feel like they are "catching up with an old friend".
All our cards in the past has always been all black, with red and we need something fresher.
The back of card, we would like just a small list of what we do i think, but if someone has a better idea, please do something cool with the back of the card:
Managed IT Services
Productivity Solutions
Data Backup and Recovery
IT System Maintenance
Managed IT Security
More details can be found on our website tqnetworks.com.au
Industry/Entity Type
It Company
Contact Information for Business Card
Name: Dwayne Falstrup
Title: Director
Phone: 03 6193 4827
Mobile: 0412 587 239
Email: dwayne@tqnetworks.com.au
Web: www.tqnetworks.com.au

```html
<!DOCTYPE html>
<html lang="en">
<head>
<meta charset="utf-8">
<title>TQ Networks – Business Cards</title>
<link rel="stylesheet" href="https://fonts.googleapis.com/css2?family=Arimo:wght@400;700&display=swap">
<style>
  :root {
    --bg: #d9d9db;
    --navy: #131b2a;
    --red: #e11b24;
    --red-deep: #9b1b28;
    --red-dark: #6c1a27;
    --white: #ffffff;
  }
  * { box-sizing: border-box; margin: 0; padding: 0; }
  html, body { width: 1200px; height: 800px; overflow: hidden; }
  body {
    background: var(--bg);
    font-family: "Arimo", Arial, sans-serif;
    position: relative;
  }
  .card {
    position: absolute;
    width: 540px;
    height: 309px;
    background: var(--navy);
    overflow: hidden;
    border-bottom: 3px solid var(--red);
    box-shadow: 0 18px 30px rgba(0,0,0,0.28);
  }
  .card--front { left: 50px; top: 245px; }
  .card--back { left: 610px; top: 245px; }

  .decor { position: absolute; inset: 0; width: 100%; height: 100%; }

  .brand {
    position: absolute;
    display: flex;
    align-items: center;
    gap: 10px;
    color: var(--red);
    font-weight: 700;
    text-transform: uppercase;
    letter-spacing: 0.5px;
    white-space: nowrap;
  }
  .brand__dot { border-radius: 50%; background: var(--red); flex: none; }
  .card--front .brand { left: 34px; top: 96px; font-size: 34px; }
  .card--front .brand__dot { width: 22px; height: 22px; }

  .person { position: absolute; left: 300px; top: 34px; }
  .person__name { color: var(--red); font-weight: 700; font-size: 21px; }
  .person__title { color: var(--white); font-size: 13px; margin-top: 3px; }

  .contacts {
    position: absolute;
    left: 38px;
    top: 178px;
    list-style: none;
    color: var(--white);
    font-size: 12.5px;
    line-height: 17px;
  }
  .contacts li { display: flex; align-items: center; gap: 8px; }
  .contacts svg { width: 11px; height: 11px; flex: none; }

  .website {
    position: absolute;
    left: 345px;
    top: 268px;
    color: var(--navy);
    font-size: 14px;
    white-space: nowrap;
    transform: rotate(-20deg);
    transform-origin: left center;
  }

  .card--back .brand {
    left: 50%;
    top: 92px;
    transform: translateX(-50%);
    font-size: 46px;
  }
  .card--back .brand__dot { width: 30px; height: 30px; }

  .services {
    position: absolute;
    left: 0; right: 0;
    top: 196px;
    color: var(--white);
    font-size: 14.5px;
    line-height: 23px;
  }
  .services__row { display: flex; justify-content: center; align-items: center; gap: 7px; }
  .tick { width: 13px; height: 13px; flex: none; }
</style>
</head>
<body>

<section class="card card--front" aria-label="Business card front">
  <svg class="decor" viewBox="0 0 540 309" preserveAspectRatio="none" role="img" aria-label="Decorative sweeping wave in dark red, red and white">
    <defs>
      <linearGradient id="decorFill" gradientUnits="userSpaceOnUse" x1="330" y1="150" x2="460" y2="300">
        <stop offset="0" stop-color="var(--red-dark)"/>
        <stop offset="0.2" stop-color="var(--red-deep)"/>
        <stop offset="0.32" stop-color="var(--red)"/>
        <stop offset="0.45" stop-color="var(--white)"/>
        <stop offset="1" stop-color="var(--white)"/>
      </linearGradient>
    </defs>
    <path d="M120 309 C 300 300, 350 100, 540 60 L540 309 Z" fill="url(#decorFill)"/>
  </svg>

  <div class="person">
    <p class="person__name">Dwayne Falstrup</p>
    <p class="person__title">Director</p>
  </div>

  <div class="brand"><span class="brand__dot"></span>TQ Networks</div>

  <ul class="contacts">
    <li>
      <svg viewBox="0 0 12 12" aria-hidden="true"><path d="M3 1 L5 3.5 L4 5 Q5 7 7 8 L8.5 7 L11 9 L9.5 11 Q4 10.5 1 3 Z" fill="var(--red)"/></svg>
      03 6193 4827
    </li>
    <li>
      <svg viewBox="0 0 12 12" aria-hidden="true"><rect x="3" y="0.5" width="6" height="11" rx="1" fill="none" stroke="var(--red)" stroke-width="1.3"/><circle cx="6" cy="9.5" r="0.8" fill="var(--red)"/></svg>
      0412 587 239
    </li>
    <li>
      <svg viewBox="0 0 12 12" aria-hidden="true"><rect x="0.5" y="2" width="11" height="8" fill="var(--red)"/><path d="M1 2.5 L6 7 L11 2.5" fill="none" stroke="var(--navy)" stroke-width="1"/></svg>
      dwayne@tqnetworks.com.au
    </li>
  </ul>

  <p class="website">www.tqnetworks.com.au</p>
</section>

<section class="card card--back" aria-label="Business card back">
  <div class="brand"><span class="brand__dot"></span>TQ Networks</div>

  <div class="services">
    <p class="services__row">
      Managed IT Services
      <svg class="tick" viewBox="0 0 14 14" aria-hidden="true"><circle cx="7" cy="7" r="7" fill="var(--red)"/><path d="M3.8 7.2 L6 9.3 L10.2 4.8" fill="none" stroke="var(--white)" stroke-width="1.6"/></svg>
      Productivity Solutions
    </p>
    <p class="services__row">
      Data Backup &amp; Recovery
      <svg class="tick" viewBox="0 0 14 14" aria-hidden="true"><circle cx="7" cy="7" r="7" fill="var(--red)"/><path d="M3.8 7.2 L6 9.3 L10.2 4.8" fill="none" stroke="var(--white)" stroke-width="1.6"/></svg>
      IT System Maintenance
      <svg class="tick" viewBox="0 0 14 14" aria-hidden="true"><circle cx="7" cy="7" r="7" fill="var(--red)"/><path d="M3.8 7.2 L6 9.3 L10.2 4.8" fill="none" stroke="var(--white)" stroke-width="1.6"/></svg>
      Managed IT Security
    </p>
  </div>
</section>

</body>
</html>
```